Falcrest security business card

Looking for a business card for my security company

Target Market(s)

Security

Industry/Entity Type

Security

Contact Information for Business Card

Name - Gil Marston. Title - General manager - direct 314 862.4490 website www. falcrestsecurityservices.example email - gil@ falcrestsecurityservices.example

Requirements
Must have
• Logo attached

```html
<!DOCTYPE html>
<html lang="en">
<head>
<meta charset="utf-8">
<title>Falcrest Security Services – Business Card</title>
<link rel="stylesheet" href="https://fonts.googleapis.com/css2?family=Montserrat:wght@400;500;700;800&display=swap">
<style>
  :root {
    --backdrop: #1b1b1d;
    --card-black: #0b0b0c;
    --card-white: #ffffff;
    --gold: #c69a5e;
    --ink: #111111;
    --muted: #8a8a8a;
  }
  * { box-sizing: border-box; margin: 0; padding: 0; }
  html, body { width: 1200px; height: 947px; overflow: hidden; }
  body {
    background: var(--backdrop);
    font-family: "Montserrat", sans-serif;
    position: relative;
  }
  .card {
    position: absolute;
    border-radius: 18px;
    overflow: hidden;
    box-shadow: 0 18px 40px rgba(0,0,0,.45);
  }

  /* Front */
  .card-front {
    left: 70px; top: 302px;
    width: 600px; height: 343px;
    background: var(--card-black);
    display: flex; align-items: center; justify-content: center;
  }
  .brand-name {
    color: var(--gold);
    font-weight: 800;
    text-transform: uppercase;
    letter-spacing: .04em;
    line-height: 1;
  }
  .card-front .brand-name { font-size: 76px; }

  /* Back */
  .card-back {
    left: 760px; top: 176px;
    width: 340px; height: 595px;
    background: var(--card-white);
    display: flex; flex-direction: column;
  }
  .back-header {
    height: 150px;
    background: var(--card-black);
    display: flex; align-items: center; justify-content: center;
  }
  .card-back .brand-name { font-size: 46px; }
  .back-body {
    flex: 1;
    display: flex; flex-direction: column; align-items: center;
    padding-top: 48px;
  }
  .person-name {
    font-size: 27px; font-weight: 800; color: var(--ink);
    text-transform: uppercase; letter-spacing: .02em;
  }
  .person-title {
    margin-top: 6px;
    font-size: 15px; font-weight: 400; color: var(--muted);
  }
  .divider {
    margin-top: 34px;
    width: 270px;
    display: flex; align-items: center; gap: 8px;
  }
  .divider-line { flex: 1; height: 1px; background: var(--gold); }
  .contact-icon {
    width: 18px; height: 18px; border-radius: 50%;
    background: var(--gold);
    display: flex; align-items: center; justify-content: center;
  }
  .contact-list {
    margin-top: 26px;
    list-style: none;
    text-align: center;
    font-size: 14px; line-height: 1.75; color: var(--ink);
  }
  .contact-phone { font-size: 17px; }
  .back-footer { height: 42px; background: var(--card-black); }
</style>
</head>
<body>

  <section class="card card-front" aria-label="Card front">
    <span class="brand-name">Falcrest</span>
  </section>

  <section class="card card-back" aria-label="Card back">
    <header class="back-header">
      <span class="brand-name">Falcrest</span>
    </header>

    <div class="back-body">
      <h1 class="person-name">Gil Marston</h1>
      <p class="person-title">General manager</p>

      <div class="divider">
        <span class="divider-line"></span>
        <span class="contact-icon" aria-hidden="true">
          <svg width="10" height="10" viewBox="0 0 24 24"><path fill="#fff" d="M6.6 10.8a15 15 0 0 0 6.6 6.6l2.2-2.2c.3-.3.7-.4 1-.2 1.1.4 2.3.6 3.6.6.6 0 1 .4 1 1V20c0 .6-.4 1-1 1A17 17 0 0 1 3 4c0-.6.4-1 1-1h3.5c.6 0 1 .4 1 1 0 1.3.2 2.5.6 3.6.1.3 0 .7-.2 1z"/></svg>
        </span>
        <span class="contact-icon" aria-hidden="true">
          <svg width="10" height="10" viewBox="0 0 24 24"><path fill="#fff" d="M3 5h18v14H3z"/><path fill="none" stroke="#c69a5e" stroke-width="2" d="M3 6l9 7 9-7"/></svg>
        </span>
        <span class="contact-icon" aria-hidden="true">
          <svg width="10" height="10" viewBox="0 0 24 24" fill="none" stroke="#fff" stroke-width="2"><circle cx="12" cy="12" r="9"/><path d="M3 12h18M12 3c3 3 3 15 0 18M12 3c-3 3-3 15 0 18"/></svg>
        </span>
        <span class="divider-line"></span>
      </div>

      <ul class="contact-list">
        <li class="contact-phone">314 862.4490</li>
        <li>www.falcrestsecurityservices.example</li>
        <li>gil@falcrestsecurityservices.example</li>
      </ul>
    </div>

    <footer class="back-footer"></footer>
  </section>

</body>
</html>
```